Webdesign fürs Mittagessen
Zielgruppe
Mit unserer Seite kann nach der nächsten Location suchen wo es was zu essen gibt. Das Angebot bezieht sich auf Food Trucks, Imbisse und Restaurants.
Kunden besuchen unsere Seite um dort anhand von Postleitzahlen/Städten nach Orten zu suchen wo es was zu Essen gibt.
Ebenso können Kunden mit guten Locations bei uns Stellplätze für Food Trucks anbieten.
Im angehängten Dokument sind 2 Screenshots der aktuellen Seite. Im Mittelpunkt der Seite steht die Suchfunktion. Das Design aus den Screenshots dient nicht als Orientierung, ebenso wenig wie das angehängt Logo!
Die angehängten Datei bitte ich vertraulich zu behandeln. Sie dürfen in keinster Weise weitergegeben werden oder veröffentlicht werden.
Aufgabenstellung
Das Design sollte übersichtlich und klar gestaltet sein.
Es sollte möglichst wenig knallige Farben haben.
Akzentfarben sind #E9A300 und #0A9DCD.

```html
<!DOCTYPE html>
<html lang="de">
<head>
<meta charset="utf-8">
<title>Mittagsfund – Dein Mittag finden</title>
<link rel="stylesheet" href="https://fonts.googleapis.com/css2?family=Open+Sans:ital,wght@0,300;0,400;0,600;0,700;1,600;1,700&display=swap">
<style>
  :root{
    --orange:#E9A300;
    --blue:#0A9DCD;
    --text:#555;
    --muted:#777;
    --icon:#9a9a9a;
    --field:#dcdcdc;
    --white:#fff;
  }
  *{box-sizing:border-box;margin:0;padding:0}
  html,body{width:1200px;height:1200px;overflow:hidden;background:var(--white)}
  body{font-family:"Open Sans",Arial,sans-serif;color:var(--text);position:relative}
  .abs{position:absolute}
  .topbar{left:0;top:0;width:1200px;height:13px;background:var(--blue)}
  .hero{left:0;top:13px;width:1200px;height:270px;
    background:linear-gradient(90deg,#b7c27c 0%,#d9cf9a 25%,#e8d8ae 45%,#d7c08a 60%,#e3a796 80%,#c9776d 100%)}
  .hero-photo{left:727px;top:93px;width:266px;height:190px;border-radius:40px 40px 0 0;
    background:linear-gradient(160deg,#d9a55a,#6b9a3c 50%,#e8e4dc)}
  .follow{left:245px;top:32px;font-size:10px;color:#fff;display:flex;align-items:center;gap:8px}
  .follow .dot{width:8px;height:12px;background:#fff}
  .brand{left:520px;top:30px;width:144px;height:60px;display:flex;align-items:center;justify-content:center;gap:6px;
    font-size:15px;font-weight:700;color:#fff}
  .brand .mark{width:12px;height:12px;border-radius:50%;background:#fff}
  .login{left:875px;top:33px;width:43px;height:20px;background:var(--blue);color:#fff;font-size:10px;line-height:20px;text-align:center}
  .signup{left:930px;top:33px;font-size:10px;line-height:20px;color:#444}
  .search{left:284px;top:81px;width:207px;height:186px;background:rgba(235,235,235,.75)}
  .search label{position:absolute;left:11px;font-size:12px;font-weight:300;color:#555}
  .search .field{position:absolute;left:10px;width:186px;height:19px;background:#fff}
  .search .select::after{content:"";position:absolute;right:0;top:0;width:19px;height:19px;background:#ddd}
  .search .select::before{content:"";position:absolute;right:5px;top:7px;border:4px solid transparent;border-top:5px solid #666;z-index:1}
  .search .more{position:absolute;left:12px;top:144px;font-size:9px;color:#555}
  .search .more::before{content:"";display:inline-block;width:4px;height:4px;background:#666;margin-right:4px;vertical-align:middle}
  .search .go{position:absolute;left:11px;top:156px;width:184px;height:24px;background:var(--orange);color:#fff;font-size:12px;font-weight:700;text-align:center;line-height:24px}
  .claim{left:526px;top:184px;font-size:18px;font-weight:700;color:#fff;line-height:25px;letter-spacing:.2px}
  .nav{left:0;top:283px;width:1200px;height:48px;background:var(--orange)}
  .nav-inner{position:absolute;left:208px;top:8px;width:777px;height:30px;border-top:1px solid rgba(255,255,255,.45);border-bottom:1px solid rgba(255,255,255,.45);
    display:flex;align-items:center}
  .nav-item{position:absolute;display:flex;align-items:center;gap:6px;color:#fff;font-size:14px;font-weight:300}
  .nav-item svg{width:20px;height:20px;stroke:#fff;fill:none;stroke-width:1.3}
  .body-bg{left:0;top:331px;width:1200px;height:542px;background:linear-gradient(180deg,#b9d1e6,#dde4ef 60%,#d9dcee)}
  .card{position:absolute;background:#fff;border-radius:4px}
  .card h2{position:absolute;font-size:16px;font-weight:400;color:#555;white-space:nowrap}
  .card h2 em{color:var(--blue);font-weight:700}
  .brandword{color:var(--blue);font-weight:700;font-style:italic}
  .small{font-size:9.5px;line-height:13px;color:#555}
  .welcome{left:211px;top:359px;width:473px;height:201px}
  .dish{position:absolute;left:26px;display:flex;align-items:center;gap:5px;font-size:12.5px;font-weight:700;font-style:italic;color:var(--orange)}
  .dish i{width:12px;height:12px;border-radius:50%;background:#aaa}
  .bubbles{position:absolute;left:188px;top:67px}
  .newsletter{left:697px;top:359px;width:280px;height:201px}
  .email{position:absolute;left:20px;top:62px;width:241px;height:24px;background:var(--field);font-size:10.5px;color:#666;line-height:24px;padding-left:8px}
  .order{position:absolute;left:20px;top:95px;width:241px;height:24px;background:var(--orange);color:#fff;font-size:12px;text-align:center;line-height:24px}
  .offer{left:211px;top:577px;width:280px;height:202px}
  .offer h3{position:absolute;left:0;top:16px;width:100%;text-align:center;font-size:16px;font-weight:700;font-style:italic;color:var(--blue)}
  .offer-art{position:absolute;left:62px;top:50px;width:157px;height:110px;border-radius:30px 30px 20px 8px;background:linear-gradient(180deg,#a9a9a9,#8e8e8e)}
  .offer .caption{position:absolute;left:0;top:174px;width:100%;text-align:center}
  .about{left:501px;top:577px;width:473px;height:202px}
  .about p{position:absolute;left:37px;width:410px}
  .partners{left:211px;top:796px;width:763px;height:77px;border-radius:4px 4px 0 0}
  .partner{position:absolute;top:34px;height:44px;background:#b5b5b5;border-radius:4px}
  .footer-links{left:225px;top:899px;font-size:8px;color:#444}
  .social{top:899px;display:flex;gap:10px}
  .social i{display:block;width:10px;height:10px;border-radius:50%;background:#888}
</style>
</head>
<body>
  <div class="abs topbar"></div>
  <div class="abs hero" role="img" aria-label="Unscharfes Foto einer Essensszene in Grün- und Warmtönen"></div>
  <div class="abs hero-photo" role="img" aria-label="Foto: Burger, Salatstapel und Getränkebecher"></div>

  <div class="abs follow">Finde uns auf <span class="dot"></span></div>
  <div class="abs brand"><span class="mark"></span>Mittagsfund</div>
  <div class="abs login">Login</div>
  <div class="abs signup">Anmelden</div>

  <form class="abs search">
    <label style="top:7px">Dein aktueller Standort</label>
    <div class="field" style="top:30px"></div>
    <label style="top:51px">Was schmeckt Ihnen ?</label>
    <div class="field select" style="top:73px"></div>
    <label style="top:94px">Aktueller Tag ?</label>
    <div class="field select" style="top:115px"></div>
    <div class="more">Erweiterete Suche</div>
    <div class="go">JETZT LOUNGE FINDEN</div>
  </form>

  <div class="abs claim">JETZT ONLINE<br>DEIN MITTAG FINDEN!</div>

  <nav class="abs nav">
    <div class="nav-inner">
      <div class="nav-item" style="left:24px"><svg viewBox="0 0 20 20"><path d="M2 10 L10 2 L18 10 M4 8 V18 H16 V8"/></svg>Home</div>
      <div class="nav-item" style="left:124px"><svg viewBox="0 0 20 20"><rect x="3" y="3" width="14" height="12" rx="2"/><circle cx="6" cy="17" r="1.5"/><circle cx="14" cy="17" r="1.5"/></svg>FoodTrucks</div>
      <div class="nav-item" style="left:267px"><svg viewBox="0 0 20 20"><path d="M3 8 Q10 1 17 8 Z M3 11 H17 M3 14 H17 V17 H3 Z"/></svg>Imbisse</div>
      <div class="nav-item" style="left:378px"><svg viewBox="0 0 24 20"><path d="M2 17 H22 M4 16 Q12 2 20 16 M12 5 V3"/></svg>Restaurants</div>
      <div class="nav-item" style="left:528px"><svg viewBox="0 0 20 20"><path d="M2 11 L11 2 H18 V9 L9 18 Z"/><circle cx="14" cy="6" r="1.3"/></svg>Kosten</div>
      <div class="nav-item" style="left:654px"><svg viewBox="0 0 20 20"><circle cx="10" cy="6" r="4"/><path d="M4 18 Q4 10 10 10 Q16 10 16 18 Z"/></svg>Über Uns</div>
    </div>
  </nav>

  <div class="abs body-bg"></div>

  <section class="card welcome">
    <svg class="abs" style="left:29px;top:13px" width="12" height="18" viewBox="0 0 12 18"><path d="M6 0 A6 6 0 0 1 12 6 C12 10 6 18 6 18 C6 18 0 10 0 6 A6 6 0 0 1 6 0 Z" fill="#9a9a9a"/><circle cx="6" cy="6" r="2.2" fill="#fff"/></svg>
    <h2 style="left:53px;top:11px">Herzlich Willkommen <em>Mittagsfund</em></h2>
    <p class="abs" style="left:25px;top:40px;font-size:12.5px;font-weight:300;color:#555">Wissen Sie schon was es gleich zum Mittag gibt ?</p>
    <div class="dish" style="top:79px"><i></i>Pizza ?</div>
    <div class="dish" style="top:101px"><i></i>Cheesburger ?</div>
    <div class="dish" style="top:123px"><i></i>Vegearisches ?</div>
    <svg class="bubbles" width="200" height="90" viewBox="0 0 200 90" font-family="Open Sans, sans-serif" font-size="7" font-style="italic" font-weight="600" fill="#888">
      <g fill="none" stroke="#aaa" stroke-width="1">
        <ellipse cx="39" cy="24" rx="36" ry="24"/>
        <ellipse cx="127" cy="37" rx="36" ry="24"/>
        <ellipse cx="81" cy="64" rx="26" ry="21"/>
      </g>
      <text x="17" y="22">„Wieder so</text><text x="17" y="32">lange warten.“</text>
      <text x="106" y="37">„Schon wieder</text><text x="106" y="47">das Selbe.“</text>
      <text x="69" y="62">„Wo</text><text x="69" y="72">denn?“</text>
    </svg>
    <p class="abs small" style="left:25px;top:157px;width:430px"><span class="brandword">Mittagsfund</span> kümmert sich Dich. Von uns erfährst Von Uns erfährst du wo die nächste Location ist die dich satt macht. So gibt es endlich mal Abwechslung in deiner Pause.</p>
  </section>

  <section class="card newsletter">
    <svg class="abs" style="left:20px;top:15px" width="19" height="13" viewBox="0 0 19 13"><rect x=".5" y=".5" width="18" height="12" fill="none" stroke="#9a9a9a"/><path d="M.5 .5 L9.5 8 L18.5 .5" fill="none" stroke="#9a9a9a"/></svg>
    <h2 style="left:47px;top:11px">Newsltter empfangen?</h2>
    <div class="email">Ihre E-Mailadresse hier eintragen</div>
    <div class="order">Jetzt bestellen</div>
    <p class="abs small" style="left:23px;top:141px;width:225px">Der Newsletter informiert dich über Events rund um das ( mobile) Essen...</p>
  </section>

  <section class="card offer">
    <h3>Valentin Veggie Bürger</h3>
    <svg class="abs" style="left:22px;top:90px" width="14" height="34" viewBox="0 0 14 34"><path d="M12 1 L2 17 L12 33" fill="none" stroke="#E9A300" stroke-width="2"/></svg>
    <svg class="abs" style="left:244px;top:90px" width="14" height="34" viewBox="0 0 14 34"><path d="M2 1 L12 17 L2 33" fill="none" stroke="#E9A300" stroke-width="2"/></svg>
    <div class="offer-art" role="img" aria-label="Illustration: Burger mit Pommes"></div>
    <p class="caption small">„Lecker mit frischen Salat und Hausmannsoße<br>innerhalb von 5 min fertig“</p>
  </section>

  <section class="card about">
    <svg class="abs" style="left:22px;top:15px" width="12" height="16" viewBox="0 0 12 16"><circle cx="6" cy="4" r="4" fill="#9a9a9a"/><path d="M0 16 Q0 8 6 8 Q12 8 12 16 Z" fill="#9a9a9a"/></svg>
    <h2 style="left:36px;top:11px">Was ist <em>Mittagsfund?</em></h2>
    <p class="small" style="top:54px"><span class="brandword">Mittagsfund</span> beherbergt aktuell 9 Food Trucks/Imbisse/Restaurants über ganz Deutschland verteilt. Insgesamt werden von Ihnen an 8 Standorten Speisen aller Art angeboten.</p>
    <p class="small" style="top:92px">Insgesamt wurden auf <span class="brandword">Mittagsfund</span> bereits 11 Bewertungen und 0 Events eingetragen.</p>
    <p class="small" style="top:118px">Das Special für Food Trucks sind unsere aktuell 1 angebotenen Stellplätze.</p>
    <p class="small" style="top:143px;width:370px">Hier kann man neue lukrative Verkaufspunkte finden und direkt mit dem Anbieter in Kontakt treten.</p>
  </section>

  <section class="card partners">
    <svg class="abs" style="left:15px;top:10px" width="16" height="16" viewBox="0 0 16 16"><path d="M8 0 L10 6 L16 6 L11 10 L13 16 L8 12 L3 16 L5 10 L0 6 L6 6 Z" fill="#9a9a9a"/></svg>
    <h2 style="left:42px;top:7px">Unsere Partner</h2>
    <div class="partner" style="left:56px;width:101px"></div>
    <div class="partner" style="left:187px;width:32px"></div>
    <div class="partner" style="left:262px;width:159px;height:34px;top:40px"></div>
    <div class="partner" style="left:459px;width:89px"></div>
    <div class="partner" style="left:584px;width:126px"></div>
  </section>

  <div class="abs footer-links">Impressum &nbsp;I AGB &nbsp;I Kontakt</div>
  <div class="abs social" style="left:913px"><i></i><i></i><i></i></div>
</body>
</html>
```